Power Point Template Design for Consulting Company
Verdant Ridge Inc.
Helping Clients Achieve Explosive Sales
Need a slide master incorporating existing logo for all regular Power Point slide layout types (title, title and content, section header, two content, comparison, title only, blank, content with caption, picture with caption)
Corporate client presentations and professional association speaking engagements
Using Power Point 2007, Windows 7.0 O/S.
Not overpowering, prefer clean white backgrounds for better projection and printing results. Verdant Ridge Inc. Logo was designed on a previous project so all files available.
logo files in all formats
business card for reference and consistency
business letterhead for reference and consistency
business stationary coor and font for reference and consistency

```html
<!DOCTYPE html>
<html lang="en">
<head>
<meta charset="utf-8">
<title>Verdant Ridge Inc. – Presentation Template</title>
<link href="https://fonts.googleapis.com/css2?family=Open+Sans:wght@400;600&display=swap" rel="stylesheet">
<style>
  :root {
    --stage: #5a5a5c;
    --paper: #ffffff;
    --brand-blue: #1a6fc0;
    --text-grey: #9a9ca0;
    --edition-grey: #6d6f73;
    --rule: #b9bbbf;
  }
  * { margin: 0; padding: 0; box-sizing: border-box; }
  html, body { width: 1200px; height: 927px; overflow: hidden; }
  body {
    background: var(--stage);
    font-family: "Open Sans", Arial, sans-serif;
    position: relative;
  }
  .slide {
    position: absolute;
    width: 512px;
    height: 386px;
    background: var(--paper);
    overflow: hidden;
    box-shadow: 0 6px 14px rgba(0,0,0,0.35);
  }
  .slide--cover { left: 40px; top: 310px; }
  .slide--title { left: 606px; top: 88px; }
  .slide--content { left: 606px; top: 500px; }
  .slide__art { position: absolute; inset: 0; width: 100%; height: 100%; }

  .brand { position: absolute; display: flex; align-items: center; color: var(--brand-blue); font-weight: 400; white-space: nowrap; }
  .brand__mark { background: var(--brand-blue); display: block; }
  .brand--small { left: 14px; top: 26px; font-size: 11px; gap: 5px; }
  .brand--small .brand__mark { width: 14px; height: 14px; }
  .brand--large { left: 0; right: 0; top: 100px; flex-direction: column; font-size: 24px; gap: 14px; }
  .brand--large .brand__mark { width: 70px; height: 70px; }

  .edition { position: absolute; right: 14px; font-size: 7px; color: var(--edition-grey); }
  .slide--cover .edition { top: 58px; right: 22px; }
  .slide--title .edition, .slide--content .edition { top: 72px; }

  .rule { position: absolute; border-top: 1px dashed var(--rule); }
  .rule--v { border-top: 0; border-left: 1px dashed var(--rule); }

  .placeholder-title { position: absolute; left: 0; right: 0; top: 134px; text-align: center; color: var(--brand-blue); font-size: 25px; font-weight: 400; }
  .placeholder-subtitle { position: absolute; left: 0; right: 0; top: 240px; text-align: center; color: var(--text-grey); font-size: 19px; font-weight: 400; }

  .header { position: absolute; left: 68px; top: 114px; color: var(--brand-blue); font-size: 28px; font-weight: 400; }
  .body-text { position: absolute; left: 133px; top: 156px; color: var(--text-grey); font-size: 22px; }
  .bullets { position: absolute; left: 172px; top: 200px; list-style: none; color: var(--text-grey); font-size: 13px; line-height: 26px; }
  .bullets li::before { content: ""; display: inline-block; width: 6px; height: 6px; border-radius: 50%; background: var(--brand-blue); margin-right: 7px; vertical-align: middle; }
  .closing-text { position: absolute; left: 0; right: 0; top: 282px; text-align: center; color: var(--text-grey); font-size: 19px; }
</style>
</head>
<body>

<svg width="0" height="0" style="position:absolute">
  <defs>
    <linearGradient id="floor" x1="0" y1="0" x2="0" y2="1">
      <stop offset="0" stop-color="#ffffff"/>
      <stop offset="1" stop-color="#dadbde"/>
    </linearGradient>
    <linearGradient id="glow" x1="1" y1="0" x2="0.3" y2="1">
      <stop offset="0" stop-color="#e4e5e8"/>
      <stop offset="1" stop-color="#ffffff" stop-opacity="0"/>
    </linearGradient>
    <linearGradient id="band" x1="0" y1="0" x2="1" y2="0">
      <stop offset="0" stop-color="#22b1ec"/>
      <stop offset="0.45" stop-color="#1a8ad2"/>
      <stop offset="1" stop-color="#0c3f8c"/>
    </linearGradient>
    <g id="slide-art">
      <rect x="0" y="0" width="512" height="300" fill="url(#glow)"/>
      <rect x="0" y="225" width="512" height="125" fill="url(#floor)"/>
      <rect x="0" y="349" width="512" height="37" fill="url(#band)"/>
    </g>
  </defs>
</svg>

<section class="slide slide--cover">
  <svg class="slide__art" viewBox="0 0 512 386" role="img" aria-label="Soft grey light glow with blue footer band"><use href="#slide-art"/></svg>
  <p class="edition">Corporate Presentation 2016 - 17</p>
  <div class="brand brand--large"><span class="brand__mark"></span>Verdant Ridge Inc.</div>
</section>

<section class="slide slide--title">
  <svg class="slide__art" viewBox="0 0 512 386" role="img" aria-label="Soft grey light glow with blue footer band"><use href="#slide-art"/></svg>
  <div class="brand brand--small"><span class="brand__mark"></span>Verdant Ridge Inc.</div>
  <div class="rule" style="left:140px; right:14px; top:66px;"></div>
  <p class="edition">Corporate Presentation 2016 - 17</p>
  <h1 class="placeholder-title">Click to add Title</h1>
  <div class="rule" style="left:110px; right:110px; top:195px;"></div>
  <div class="rule rule--v" style="left:130px; top:200px; height:80px;"></div>
  <p class="placeholder-subtitle">Click to add Subtitle</p>
</section>

<section class="slide slide--content">
  <svg class="slide__art" viewBox="0 0 512 386" role="img" aria-label="Soft grey light glow with blue footer band"><use href="#slide-art"/></svg>
  <div class="brand brand--small"><span class="brand__mark"></span>Verdant Ridge Inc.</div>
  <div class="rule" style="left:140px; right:14px; top:66px;"></div>
  <p class="edition">Corporate Presentation 2016 - 17</p>
  <div class="rule" style="left:50px; right:40px; top:96px;"></div>
  <h2 class="header">Header 1</h2>
  <p class="body-text">Click to add text</p>
  <ul class="bullets">
    <li>Click to add text sentence 1</li>
    <li>Click to add text sentence 1</li>
  </ul>
  <div class="rule" style="left:50px; right:40px; top:268px;"></div>
  <p class="closing-text">Click to add text</p>
  <div class="rule" style="left:50px; right:40px; top:322px;"></div>
</section>

</body>
</html>
```